3月15日にガールズバーをオープン致しました。
ビルの入り口に置いて使うA1立て看板の製作をお願いします。
A4など縮小サイズでもいただけると助かります。
白を基調とした夜でも目立つ感じにしたいです。

セット料金 40分2000円 tax&service 20%

チャージのみ1時間1500円 tax&service 15

クレジットチャージ 10%
飲み放題付き (焼酎 ウイスキー カクテルなど)
ビル3階 席数17席  団体客歓迎

若いギャル系の女の子の写真を大きく入れて頂きたいのですが素材が無く
困ってます。素材をお持ちかたにお願いしたいと思ってます。

現在の看板を添付致しました。ご参考までに。
文章は記載しないでも大丈夫です。

店舗名 Sunflower(サンフラワー)です。

よろしくお願いします。
資料を再添付致しました。よろしくお願いします。
依頼金額を25000円に変更して、延長しました。
提案下さった皆様ありがとうございます。
もう少し提案を見させていただけたらと思います。

具体的なイメージをデザベース様の過去の事例で近いものを添付致しました。
よろしくお願いします。

最初に思い描いてたイメージより良かったです
女の子と背景のピンクもかわいいくて満足です。

ありがとうございました!

提案くださった皆様ありがとうございます!
修正をしてくださった皆様も早急な対応に感謝致します。

ありがとうございました!

```html
<!DOCTYPE html>
<html lang="ja">
<head>
<meta charset="utf-8">
<title>Sunflower Girls BAR</title>
<link href="https://fonts.googleapis.com/css2?family=Noto+Sans+JP:wght@500;700;900&family=Oswald:wght@600;700&display=swap" rel="stylesheet">
<style>
  :root {
    --red: #d4123f;
    --crimson: #c8103a;
    --pink: #e0437a;
    --ink: #1a1a1a;
    --paper: #ffffff;
    --skin: #e6d9d2;
    --dress: #8f1f2a;
  }
  * { margin: 0; padding: 0; box-sizing: border-box; }
  html, body { width: 855px; height: 1200px; overflow: hidden; background: var(--paper); }
  .signboard {
    position: relative; width: 855px; height: 1200px; overflow: hidden;
    background: var(--paper);
    font-family: "Noto Sans JP", sans-serif; color: var(--red);
  }
  .signboard p, .signboard h1 { position: absolute; white-space: nowrap; }
  .model-photo {
    position: absolute; left: 0; top: 0; width: 660px; height: 840px;
    background:
      linear-gradient(90deg, rgba(255,255,255,0) 45%, var(--paper) 90%),
      linear-gradient(180deg, #f4f1ef 0%, var(--skin) 30%, #cfc3bd 55%, var(--dress) 78%, #6e1620 100%);
  }
  .tagline {
    left: 18px; top: 60px;
    writing-mode: vertical-rl; font-weight: 700; font-size: 24px;
    letter-spacing: 4px; color: var(--pink);
  }
  .label { font-weight: 900; font-size: 26px; line-height: 1; }
  .price { font-weight: 900; font-size: 54px; line-height: 1; letter-spacing: -2px; }
  .note { font-weight: 700; font-size: 20px; color: var(--ink); line-height: 1; }
  .set-label { left: 356px; top: 40px; }
  .set-price { left: 352px; top: 76px; }
  .set-note { left: 505px; top: 140px; }
  .charge-label { left: 356px; top: 172px; }
  .charge-price { left: 352px; top: 208px; }
  .charge-note { left: 505px; top: 272px; }
  .credit { left: 535px; top: 310px; font-weight: 900; font-size: 20px; color: var(--ink); line-height: 1; }
  .credit-note { left: 535px; top: 336px; font-weight: 700; font-size: 14px; color: var(--ink); line-height: 1; }
  .open-label { left: 428px; top: 368px; font-weight: 900; font-size: 24px; color: var(--ink); line-height: 1; }
  .open-time { left: 424px; top: 392px; font-weight: 900; font-size: 64px; color: var(--red); line-height: 1; letter-spacing: -1px; }
  .close { left: 438px; top: 460px; font-weight: 900; font-size: 24px; color: var(--ink); line-height: 1; }
  .close b { font-size: 42px; vertical-align: -4px; }
  .shop-name {
    left: 700px; top: 14px;
    writing-mode: vertical-rl;
    font-family: "Oswald", sans-serif; font-weight: 700; font-size: 120px;
    line-height: 1; color: var(--crimson); letter-spacing: 2px;
  }
  .shop-sub {
    left: 752px; top: 628px;
    writing-mode: vertical-rl; font-weight: 900; font-size: 22px; color: var(--ink); line-height: 1;
  }
  .shop-kana {
    left: 728px; top: 628px;
    writing-mode: vertical-rl; font-weight: 900; font-size: 16px; color: var(--ink); line-height: 1;
  }
  .drinks-head { left: 346px; top: 664px; font-weight: 900; font-size: 56px; line-height: 1; }
  .drinks-detail { left: 350px; top: 734px; font-weight: 700; font-size: 19px; color: var(--ink); line-height: 1; }
  .seats { left: 350px; top: 770px; font-weight: 900; font-size: 30px; line-height: 1; }
  .floor-box {
    position: absolute; left: 45px; top: 840px; width: 787px; height: 340px;
    border: 20px solid var(--red); background: var(--paper);
    display: flex; align-items: center; justify-content: center; gap: 26px;
  }
  .floor-box .floor {
    font-family: "Oswald", sans-serif; font-weight: 700; font-size: 260px;
    line-height: 1; color: var(--red);
  }
</style>
</head>
<body>
<main class="signboard">
  <div class="model-photo" role="img" aria-label="赤いドレスを着た金髪の女性の写真(顔は写らない)"></div>

  <p class="tagline">シックで甘酸っぱいガールズバー</p>

  <p class="label set-label">セット料金</p>
  <p class="price set-price">40分2000円</p>
  <p class="note set-note">tax&amp;service 20%</p>
  <p class="label charge-label">チャージのみ</p>
  <p class="price charge-price">1時間1500円</p>
  <p class="note charge-note">tax&amp;service 15%</p>
  <p class="credit">クレジット利用可</p>
  <p class="credit-note">クレジットチャージ 10%</p>

  <p class="open-label">OPEN</p>
  <p class="open-time">20:00</p>
  <p class="close">CLOSE <b>5:00</b></p>

  <h1 class="shop-name">Sunflower</h1>
  <p class="shop-sub">Girls BAR</p>
  <p class="shop-kana">サンフラワー</p>

  <p class="drinks-head">飲み放題付</p>
  <p class="drinks-detail">[焼酎 ウイスキー カクテルなど]</p>
  <p class="seats">席数17席 団体客歓迎</p>

  <section class="floor-box">
    <span class="floor">3F</span>
    <svg class="floor-arrows" width="170" height="230" viewBox="0 0 170 230" aria-hidden="true">
      <polygon points="85,12 160,108 10,108" fill="none" stroke="var(--red)" stroke-width="16"/>
      <polygon points="85,124 160,220 10,220" fill="none" stroke="var(--red)" stroke-width="16"/>
    </svg>
  </section>
</main>
</body>
</html>
```